Seven Rising Steps - Site signage graphic

I need a large board creating to show our Seven Bright Paths plan.

I have added a previous version of this called Seven Bold Moves as well as the draft (AI) version of Seven Rising Steps and our new PowerPoint as an example of branding .

Target Market(s)

Colleagues and visitors to site

Industry/Entity Type

Food manufacturing

Font styles to use
Other font styles liked:
• Raleway Medium

Requirements
Must have
• Clear and all text as per AI mock up

```html
<!DOCTYPE html>
<html lang="en">
<head>
<meta charset="utf-8">
<title>Seven Bright Paths – Site Board</title>
<link href="https://fonts.googleapis.com/css2?family=Archivo+Black&family=Barlow+Condensed:wght@500;600&family=Montserrat:wght@800&family=Oswald:wght@500;700&family=Lora&family=Kalam:wght@400&family=Roboto:wght@400&display=swap" rel="stylesheet">
<style>
  :root {
    --green: #0f4a2c;
    --orange: #e8731e;
    --yellow: #f7b42c;
    --cream: #f8f6f1;
    --ink: #1e2a22;
    --line: #dcd8cf;
    --field: #e6e2d6;
  }
  * { box-sizing: border-box; margin: 0; padding: 0; }
  html, body { width: 1200px; height: 736px; overflow: hidden; background: var(--cream); }
  .board { position: relative; width: 1200px; height: 736px; background: var(--cream); overflow: hidden; font-family: "Roboto", sans-serif; color: var(--ink); }
  .shape { position: absolute; }

  .brand { position: absolute; left: 76px; top: 92px; display: flex; align-items: flex-start; gap: 8px; }
  .brand-name { font-family: "Montserrat", sans-serif; font-weight: 800; color: var(--green); font-size: 36px; line-height: 0.95; letter-spacing: 1px; }
  .brand-name span { display: block; }
  .brand-dot { width: 14px; height: 14px; border-radius: 50%; background: var(--green); margin-top: 4px; }

  .title { position: absolute; left: 350px; top: 66px; font-family: "Archivo Black", sans-serif; font-size: 58px; line-height: 1; color: var(--green); letter-spacing: 1px; white-space: nowrap; }
  .subtitle { position: absolute; left: 352px; top: 136px; font-family: "Montserrat", sans-serif; font-weight: 800; font-size: 22px; color: var(--green); letter-spacing: -0.3px; white-space: nowrap; }
  .tagline { position: absolute; left: 350px; top: 170px; width: 520px; display: flex; align-items: center; gap: 18px; }
  .tagline .rule { flex: 1; height: 1.5px; background: var(--yellow); }
  .tagline p { font-family: "Lora", serif; font-size: 18px; color: var(--ink); white-space: nowrap; }
  .tagline em { font-family: "Kalam", cursive; font-style: normal; color: var(--yellow); font-size: 17px; }

  .priorities { position: absolute; left: 45px; top: 214px; display: flex; gap: 16px; }
  .card { position: relative; width: 214px; height: 317px; background: var(--cream); border: 1px solid var(--line); border-top: 0; }
  .card::before { content: ""; position: absolute; left: -1px; right: -1px; top: 0; height: 9px; background: var(--green); }
  .card.is-orange::before { background: var(--orange); }
  .card-number { position: absolute; left: 16px; top: 22px; font-family: "Oswald", sans-serif; font-weight: 700; font-size: 112px; line-height: 1; color: var(--green); }
  .is-orange .card-number { color: var(--orange); }
  .card-icon { position: absolute; left: 106px; top: 26px; width: 86px; height: 86px; }
  .card-title { position: absolute; left: 17px; top: 135px; right: 10px; font-family: "Barlow Condensed", sans-serif; font-weight: 600; font-size: 19px; line-height: 1.1; color: var(--green); text-transform: uppercase; }
  .card-lead { font-family: "Barlow Condensed", sans-serif; font-weight: 500; font-size: 13.5px; line-height: 1.2; text-transform: uppercase; color: var(--yellow); margin-top: 10px; }
  .is-orange .card-lead { color: var(--orange); }
  .card-copy { font-family: "Roboto", sans-serif; font-size: 9.6px; line-height: 1.38; color: var(--ink); margin-top: 10px; text-transform: none; font-weight: 400; }

  .scene { position: absolute; left: 0; top: 598px; width: 650px; height: 138px; background: linear-gradient(180deg, var(--cream) 0%, var(--field) 100%); }

  .footer-item { position: absolute; display: flex; align-items: center; gap: 12px; }
  .footer-item svg { flex: none; }
  .footer-text { font-family: "Barlow Condensed", sans-serif; font-weight: 500; font-size: 18px; line-height: 1.15; color: var(--green); text-transform: uppercase; }
  .footer-text .accent { color: var(--yellow); }
  .footer-rule { position: absolute; top: 620px; width: 1px; height: 62px; background: var(--ink); opacity: 0.6; }
  .sign-off { position: absolute; left: 1064px; top: 618px; font-family: "Kalam", cursive; font-size: 20px; line-height: 1.25; color: var(--yellow); }
</style>
</head>
<body>
<div class="board">
  <svg class="shape" style="left:0;top:0" width="220" height="85" viewBox="0 0 220 85"><polygon points="0,0 212,0 0,82" fill="var(--yellow)"/></svg>
  <svg class="shape" style="left:1080px;top:0" width="120" height="230" viewBox="0 0 120 230">
    <polygon points="40,0 80,0 30,120" fill="var(--yellow)"/>
    <polygon points="95,8 120,30 55,72" fill="var(--orange)"/>
    <polygon points="120,65 120,95 90,75" fill="var(--yellow)"/>
    <polygon points="20,135 120,112 120,160" fill="var(--orange)"/>
    <polygon points="40,160 110,190 100,222" fill="var(--yellow)"/>
  </svg>
  <svg class="shape" style="left:1080px;top:600px" width="120" height="136" viewBox="0 0 120 136"><polygon points="120,0 120,136 0,136" fill="var(--yellow)"/></svg>

  <div class="brand">
    <div class="brand-name"><span>CORVANE</span><span>FOODS</span></div>
    <div class="brand-dot"></div>
  </div>

  <h1 class="title">SEVEN BRIGHT PATHS</h1>
  <h2 class="subtitle">FROM CHEESEMAKERS TO CHANGEMAKERS</h2>
  <div class="tagline"><span class="rule"></span><p>Proud of our heritage. <em>Focused on our future.</em></p><span class="rule"></span></div>

  <div class="priorities">
    <article class="card">
      <div class="card-number">1</div>
      <svg class="card-icon" viewBox="0 0 86 86" role="img" aria-label="Icon of a farmer with a pitchfork"><circle cx="43" cy="43" r="41.5" fill="none" stroke="var(--green)" stroke-width="1.6"/><circle cx="43" cy="43" r="26" fill="var(--green)" opacity="0.15"/></svg>
      <h3 class="card-title">People, places<br>&amp; products
        <p class="card-lead">We do things the right way</p>
        <p class="card-copy">Our success starts with great people, strong communities and quality milk. We are committed to producing food responsibly, supporting our farming partners and creating opportunities for future generations.</p>
      </h3>
    </article>
    <article class="card is-orange">
      <div class="card-number">2</div>
      <svg class="card-icon" viewBox="0 0 86 86" aria-hidden="true"><circle cx="43" cy="43" r="41.5" fill="none" stroke="var(--orange)" stroke-width="1.6"/><path d="M43 20 L61 27 V42 C61 54 53 62 43 66 C33 62 25 54 25 42 V27 Z" fill="none" stroke="var(--orange)" stroke-width="2.2" stroke-linejoin="round"/><circle cx="43" cy="42" r="9" fill="none" stroke="var(--orange)" stroke-width="2"/><path d="M38.5 42 L42 45.5 L48 38.5" fill="none" stroke="var(--orange)" stroke-width="2" stroke-linecap="round"/></svg>
      <h3 class="card-title">Cyber security
        <p class="card-lead">Protecting what matters</p>
        <p class="card-copy">Every colleague plays a role in keeping our information, systems and customers safe. Strong cyber security protects our business today and supports our future growth.</p>
      </h3>
    </article>
    <article class="card">
      <div class="card-number">3</div>
      <svg class="card-icon" viewBox="0 0 86 86" aria-hidden="true"><circle cx="43" cy="43" r="41.5" fill="none" stroke="var(--green)" stroke-width="1.6"/><path d="M35 48 L28 64 L34 62 L37 68 L42 54 M51 48 L58 64 L52 62 L49 68 L44 54" fill="none" stroke="var(--green)" stroke-width="2" stroke-linejoin="round"/><circle cx="43" cy="38" r="16" fill="var(--cream)" stroke="var(--green)" stroke-width="2"/><circle cx="43" cy="38" r="10" fill="none" stroke="var(--green)" stroke-width="1.6"/><polygon points="43,32 44.8,36 49,36.3 45.8,39 46.8,43 43,40.8 39.2,43 40.2,39 37,36.3 41.2,36" fill="none" stroke="var(--green)" stroke-width="1.3"/></svg>
      <h3 class="card-title">Quality &amp; continuous<br>improvement
        <p class="card-lead">Be the best at what we do</p>
        <p class="card-copy">Quality and food safety are at the heart of everything we do. By continually improving our processes, reducing waste and learning every day, we deliver products our customers can trust.</p>
      </h3>
    </article>
    <article class="card is-orange">
      <div class="card-number">4</div>
      <svg class="card-icon" viewBox="0 0 86 86" role="img" aria-label="Icon of a handshake"><circle cx="43" cy="43" r="41.5" fill="none" stroke="var(--orange)" stroke-width="1.6"/><rect x="20" y="34" width="46" height="18" rx="9" fill="var(--orange)" opacity="0.18"/></svg>
      <h3 class="card-title">Customer focus
        <p class="card-lead" style="margin-top:38px">Build trust. Create value<br>for the long term.</p>
        <p class="card-copy">We build strong, long-term relationships based on trust by understanding our customers’ needs and working together to deliver outstanding value.</p>
      </h3>
    </article>
    <article class="card">
      <div class="card-number">5</div>
      <svg class="card-icon" viewBox="0 0 86 86" aria-hidden="true"><circle cx="43" cy="43" r="41.5" fill="none" stroke="var(--green)" stroke-width="1.6"/><path d="M36 52 C36 46 31 44 31 37 A12 12 0 0 1 55 37 C55 44 50 46 50 52 Z" fill="none" stroke="var(--green)" stroke-width="2" stroke-linejoin="round"/><path d="M37 56 H49 M39 60 H47" stroke="var(--green)" stroke-width="2" stroke-linecap="round"/><path d="M43 16 V20 M25 25 L28 28 M61 25 L58 28 M18 39 H22 M64 39 H68 M24 54 L27 51 M62 54 L59 51" stroke="var(--green)" stroke-width="2" stroke-linecap="round"/></svg>
      <h3 class="card-title">Transformation<br>&amp; innovation
        <p class="card-lead">Shaping tomorrow, today</p>
        <p class="card-copy">We challenge ourselves to think differently, embrace change and never stand still. Through innovation, collaboration and continuous improvement, we will build a stronger, smarter and more sustainable Corvane Foods for the future.</p>
      </h3>
    </article>
  </div>

  <div class="scene" role="img" aria-label="Line sketch of a farm with barns, silo, trees, rolling hills and grazing cows"></div>

  <div class="footer-item" style="left:486px;top:620px">
    <svg width="60" height="60" viewBox="0 0 60 60" aria-hidden="true"><circle cx="30" cy="30" r="28.5" fill="var(--cream)" stroke="var(--green)" stroke-width="1.6"/><path d="M19 42 L37 24 M41 16 L44 19 M37 17 L44 24 M34 20 L40 26" stroke="var(--green)" stroke-width="2" stroke-linecap="round"/><ellipse cx="22" cy="21" rx="4.5" ry="6" transform="rotate(-45 22 21)" fill="none" stroke="var(--green)" stroke-width="2"/><path d="M26 25 L41 42" stroke="var(--green)" stroke-width="2" stroke-linecap="round"/></svg>
    <p class="footer-text">From farm to fork.<br><span class="accent">We’re shaping the industry.</span></p>
  </div>
  <span class="footer-rule" style="left:818px"></span>
  <div class="footer-item" style="left:840px;top:620px">
    <svg width="60" height="60" viewBox="0 0 60 60" aria-hidden="true"><circle cx="30" cy="30" r="28.5" fill="none" stroke="var(--green)" stroke-width="1.6"/><circle cx="30" cy="24" r="4.5" fill="none" stroke="var(--green)" stroke-width="1.8"/><circle cx="20" cy="27" r="3.5" fill="none" stroke="var(--green)" stroke-width="1.8"/><circle cx="40" cy="27" r="3.5" fill="none" stroke="var(--green)" stroke-width="1.8"/><path d="M22 40 C22 33 38 33 38 40 M13 40 C13 35 20 33 23 34 M47 40 C47 35 40 33 37 34" fill="none" stroke="var(--green)" stroke-width="1.8" stroke-linecap="round"/></svg>
    <p class="footer-text">One business.<br>One purpose.<br>Dive priorities.</p>
  </div>
  <span class="footer-rule" style="left:1043px"></span>
  <p class="sign-off">Let’s thrive<br>&nbsp;&nbsp;together</p>
  <svg class="shape" style="left:1120px;top:664px" width="50" height="26" viewBox="0 0 50 26" aria-hidden="true"><path d="M2 24 C14 12 30 4 48 2" fill="none" stroke="var(--green)" stroke-width="1.6" stroke-linecap="round"/></svg>
</div>
</body>
</html>
```